Brevik Electric Business Card

An electrical contractor needs a business card design, that will stand out.
I would like designs that use the colors in the logo shown. The logo attached I am ok with but if you have a better idea I am open for suggestions. I like the color scheme.
Industry/Entity Type
Electrical
Contact Information for Business Card
Services, social media, QR code,

```html
<!DOCTYPE html>
<html lang="en">
<head>
<meta charset="utf-8">
<title>Brevik Electric Business Card</title>
<link rel="stylesheet" href="https://fonts.googleapis.com/css2?family=Montserrat:wght@400;500;700&display=swap">
<style>
  :root {
    --bg: #c4c4c4;
    --white: #ffffff;
    --black: #141414;
    --ink: #1e1e1e;
    --yellow: #f2b707;
    --grey-text: #2a2a2a;
  }
  * { box-sizing: border-box; margin: 0; padding: 0; }
  html, body { width: 1200px; height: 800px; overflow: hidden; }
  body {
    background: var(--bg);
    font-family: "Montserrat", Arial, sans-serif;
    position: relative;
  }
  .card {
    position: absolute;
    top: 235px;
    width: 540px;
    height: 320px;
    border-radius: 22px;
    overflow: hidden;
  }
  /* Front */
  .card-front {
    left: 40px;
    background: var(--white);
    border-bottom: 5px solid var(--yellow);
  }
  .corner-block {
    position: absolute;
    top: 0; right: 0;
    width: 78px; height: 60px;
    background: var(--yellow);
  }
  .social-row {
    position: absolute;
    top: 22px; right: 100px;
    display: flex; gap: 8px;
  }
  .social-dot {
    width: 20px; height: 20px; border-radius: 50%;
    background: var(--ink);
  }
  .person {
    position: absolute;
    left: 34px; top: 82px;
  }
  .person-name {
    font-weight: 700; font-size: 21px; letter-spacing: 0.5px;
    color: var(--ink);
  }
  .person-role {
    font-weight: 500; font-size: 13px; letter-spacing: 1px;
    color: var(--yellow); margin-top: 4px;
  }
  .contact-band {
    position: absolute;
    left: 0; top: 146px;
    width: 300px; height: 82px;
    background: var(--black);
    padding: 12px 0 0 34px;
  }
  .contact-line {
    display: flex; align-items: center; gap: 9px;
    color: var(--white); font-size: 13px; font-weight: 500;
    line-height: 20px;
  }
  .contact-line svg { width: 13px; height: 13px; flex: none; }
  .address {
    position: absolute;
    left: 34px; top: 246px;
    font-size: 14px; color: var(--grey-text); line-height: 20px;
  }
  .brand-front {
    position: absolute;
    left: 318px; top: 86px;
    width: 200px;
    display: flex; flex-direction: column; align-items: center; gap: 12px;
  }
  .brand-mark {
    width: 96px; height: 96px; border-radius: 50%;
    border: 6px solid var(--yellow);
  }
  .brand-name-front {
    font-weight: 700; font-size: 17px; letter-spacing: 0.5px;
    color: var(--ink); text-transform: uppercase;
    white-space: nowrap;
  }
  /* Back */
  .card-back {
    left: 620px;
    background: var(--black);
  }
  .brand-back {
    position: absolute;
    left: 0; right: 0; top: 48px;
    display: flex; flex-direction: column; align-items: center;
  }
  .brand-back .brand-mark { width: 110px; height: 110px; }
  .brand-name-back {
    margin-top: 22px;
    font-weight: 700; font-size: 32px; letter-spacing: 1px;
    color: var(--white); text-transform: uppercase;
    white-space: nowrap;
  }
  .social-outline-row {
    margin-top: 18px;
    display: flex; align-items: center; gap: 14px;
  }
  .rule { width: 50px; height: 1.5px; background: var(--yellow); }
  .social-ring {
    width: 34px; height: 34px; border-radius: 50%;
    border: 2px solid var(--yellow);
  }
</style>
</head>
<body>
  <section class="card card-front">
    <div class="corner-block"></div>
    <div class="social-row">
      <span class="social-dot"></span><span class="social-dot"></span><span class="social-dot"></span>
    </div>
    <div class="person">
      <p class="person-name">MARTEN HALE</p>
      <p class="person-role">MANAGING DIRECTOR</p>
    </div>
    <div class="contact-band">
      <p class="contact-line">
        <svg viewBox="0 0 16 16"><path d="M4 1l3 3-2 2c1 2 3 4 5 5l2-2 3 3-2 3C7 15 1 9 1 3z" fill="#f2b707"/></svg>
        044-555 019 284
      </p>
      <p class="contact-line">
        <svg viewBox="0 0 16 16"><rect x="1" y="3" width="14" height="10" fill="#f2b707"/><path d="M1 3l7 6 7-6" stroke="#141414" stroke-width="1.5" fill="none"/></svg>
        info@brevikelectric.com
      </p>
      <p class="contact-line">
        <svg viewBox="0 0 16 16"><circle cx="8" cy="8" r="7" fill="#f2b707"/><path d="M1 8h14M8 1v14M3 4h10M3 12h10" stroke="#141414" stroke-width="1"/></svg>
        www.brevikelectric.com
      </p>
    </div>
    <p class="address">27, Foundry Lane, Unit 9<br>60318, Northmoor</p>
    <div class="brand-front">
      <span class="brand-mark"></span>
      <p class="brand-name-front">Brevik Electric</p>
    </div>
  </section>

  <section class="card card-back">
    <div class="brand-back">
      <span class="brand-mark"></span>
      <p class="brand-name-back">Brevik Electric</p>
      <div class="social-outline-row">
        <span class="rule"></span>
        <span class="social-ring"></span>
        <span class="social-ring"></span>
        <span class="social-ring"></span>
        <span class="social-ring"></span>
        <span class="rule"></span>
      </div>
    </div>
  </section>
</body>
</html>
```